Flyer für einen Pflegedienst
Zielgruppe
Wir sind ein Pflegedienst, unsere Zielgruppe sind alle Menschen die Unterstützung brauchen. Das sind im Hauptteil Senioren.
Aufgabenstellung
Der Flyer soll im DIN A5 Format designed sein. Der Print soll hochwertig sein. Wir möchten vor allem wohlhabendere Kunden damit ansprechen. Er soll die Kunden direkt packen, aber auch nicht zu viele Informationen beinhalten, die einen überfordern.

```html
<!DOCTYPE html>
<html lang="de">
<head>
<meta charset="utf-8">
<title>Pflege Varnholt – Flyer</title>
<link rel="stylesheet" href="https://fonts.googleapis.com/css2?family=Pacifico&family=Plus+Jakarta+Sans:wght@500;600;700;800&display=swap">
<style>
  :root{
    --green:#2a8545;
    --green-light:#46b04c;
    --sage:#c8dccb;
    --orange:#f07237;
    --text:#4a4a4a;
    --ink:#1c1c1c;
    --white:#ffffff;
    --page:#ececec;
  }
  *{box-sizing:border-box;margin:0;padding:0}
  html,body{width:1101px;height:1200px;overflow:hidden;background:var(--page)}
  body{font-family:"Plus Jakarta Sans",sans-serif;color:var(--text)}
  .flyer{position:absolute;left:141px;top:20px;width:818px;height:1160px;overflow:hidden;
    background:radial-gradient(ellipse at 40% 62%,#ffffff 0%,#f3f7f4 45%,#d6e6da 100%)}
  .hero-photo{position:absolute;left:0;top:0;width:818px;height:720px;
    background:linear-gradient(100deg,#e9e9ea 0%,#e4e4e6 45%,#c9cdd3 62%,#a9b7c4 78%,#7fa9cf 100%);
    -webkit-mask-image:linear-gradient(180deg,#000 0%,#000 78%,transparent 100%);
    mask-image:linear-gradient(180deg,#000 0%,#000 78%,transparent 100%)}
  .brand{position:absolute;left:36px;top:46px;width:360px;text-align:center}
  .brand-mark{width:96px;height:96px;border-radius:50%;border:6px solid var(--ink);margin:0 auto 18px}
  .brand-name{font-size:40px;font-weight:800;color:var(--ink);letter-spacing:-0.5px;line-height:1}
  .brand-tagline{font-size:16px;font-weight:500;color:var(--ink);margin-top:12px}
  .shapes{position:absolute;left:0;top:0}
  .headline{position:absolute;left:52px;top:318px;color:var(--white)}
  .headline-script{font-family:"Pacifico",cursive;font-size:70px;line-height:92px;
    text-shadow:3px 3px 0 rgba(0,0,0,.18)}
  .headline-sub{font-size:29px;font-weight:700;margin-top:-4px}
  .benefits{position:absolute;left:52px;top:606px;list-style:none}
  .benefits li{display:flex;align-items:center;gap:24px;height:30.5px;font-size:16.5px;font-weight:700;color:#454545;letter-spacing:.2px}
  .tick{width:17px;height:17px;flex:none}
  .service-rule{position:absolute;left:54px;top:743px;width:714px;height:2px;background:var(--sage)}
  .service-pill{position:absolute;left:286px;top:720px;width:248px;height:50px;border-radius:25px;
    background:var(--orange);border:4px solid var(--sage);color:var(--white);
    font-size:24px;font-weight:700;display:flex;align-items:center;justify-content:center}
  .service{position:absolute;top:782px}
  .service-head{display:flex;align-items:center;gap:14px;height:56px;margin-bottom:16px}
  .service-icon{width:50px;height:50px;flex:none;border-radius:50%;background:var(--sage);
    display:flex;align-items:center;justify-content:center}
  .service-title{font-size:19px;font-weight:800;color:var(--green);line-height:1.35}
  .service-list{list-style:none}
  .service-list li{position:relative;padding-left:32px;font-size:14.5px;font-weight:500;line-height:19.5px;color:#4d4d4d;margin-bottom:18px;letter-spacing:.3px}
  .service-list li::before{content:"";position:absolute;left:2px;top:5px;border-left:9px solid var(--orange);
    border-top:5px solid transparent;border-bottom:5px solid transparent}
  .col-care{left:52px;width:204px}
  .col-home{left:287px;width:222px}
  .col-basic{left:547px;width:236px}
  .footer{position:absolute;left:0;bottom:0;width:818px;height:48px;display:flex;align-items:center;
    justify-content:space-between;padding:0 48px 0 52px;color:var(--white);font-size:17.5px;font-weight:700}
  .contact{display:flex;align-items:center;gap:14px}
  .contact svg{width:18px;height:18px;flex:none}
</style>
</head>
<body>
<main class="flyer">
  <div class="hero-photo" role="img" aria-label="Foto: lächelnde Seniorin im Rollstuhl, dahinter eine Pflegekraft in blauer Kleidung mit Stethoskop"></div>

  <header class="brand">
    <div class="brand-mark"></div>
    <div class="brand-name">Pflege Varnholt</div>
    <div class="brand-tagline">Mit Herz betreut, sicher umsorgt</div>
  </header>

  <svg class="shapes" width="818" height="1160" viewBox="0 0 818 1160">
    <defs>
      <linearGradient id="bannerGreen" x1="0" y1="1" x2="1" y2="0">
        <stop offset="0" stop-color="#237a3e"/>
        <stop offset="0.6" stop-color="#2a8545"/>
        <stop offset="1" stop-color="#46b04c"/>
      </linearGradient>
      <linearGradient id="swooshGreen" x1="0" y1="0" x2="1" y2="0">
        <stop offset="0" stop-color="#237a3e"/>
        <stop offset="1" stop-color="#46b04c"/>
      </linearGradient>
    </defs>
    <path d="M392 560 C400 640 470 700 560 690 C660 680 760 640 818 590 L818 560 C740 620 650 660 560 660 C470 660 410 620 392 560Z" fill="var(--sage)"/>
    <path d="M392 545 C398 610 460 660 560 652 C660 644 760 580 818 495 L818 530 C760 610 660 670 560 673 C460 676 392 630 392 545Z" fill="url(#swooshGreen)"/>
    <path d="M0 322 C120 284 260 276 420 292 C470 298 484 322 478 352 L462 520 C458 548 440 560 405 562 C260 566 110 578 0 608Z" fill="url(#bannerGreen)"/>
  </svg>

  <section class="headline">
    <div class="headline-script">Pflegedienst<br>in Mülheim</div>
    <div class="headline-sub">an der Ruhr &amp; Umgebung</div>
  </section>

  <ul class="benefits">
    <li><svg class="tick" viewBox="0 0 20 20"><circle cx="10" cy="10" r="10" fill="#f07237"/><path d="M5.5 10.5l3 3 6-6.5" fill="none" stroke="#fff" stroke-width="2.4" stroke-linecap="round" stroke-linejoin="round"/></svg>Zuverlässige ambulante Pflege</li>
    <li><svg class="tick" viewBox="0 0 20 20"><circle cx="10" cy="10" r="10" fill="#f07237"/><path d="M5.5 10.5l3 3 6-6.5" fill="none" stroke="#fff" stroke-width="2.4" stroke-linecap="round" stroke-linejoin="round"/></svg>Schnelle Aufnahme ohne Wartezeit</li>
    <li><svg class="tick" viewBox="0 0 20 20"><circle cx="10" cy="10" r="10" fill="#f07237"/><path d="M5.5 10.5l3 3 6-6.5" fill="none" stroke="#fff" stroke-width="2.4" stroke-linecap="round" stroke-linejoin="round"/></svg>Experten für chronische &amp; akute Wunden</li>
  </ul>

  <div class="service-rule"></div>
  <div class="service-pill">Unser Service</div>

  <section class="service col-care">
    <div class="service-head">
      <div class="service-icon"><svg width="28" height="26" viewBox="0 0 28 26"><path d="M14 25C5 18 1 13 1 8a6.5 6.5 0 0 1 13-1 6.5 6.5 0 0 1 13 1c0 5-4 10-13 17z" fill="#2a8545"/><path d="M12 8h4v3.5h3.5v4H16V19h-4v-3.5H8.5v-4H12z" fill="#fff"/></svg></div>
      <div class="service-title">Behandlungs<br>pflege</div>
    </div>
    <ul class="service-list">
      <li>Professionelle Wundversorgung und Verbandswechsel</li>
      <li>Zuverlässige Medikamentengabe und Injektionen</li>
      <li>Auf individuelle Bedürfnisse abgestimmte Pflege</li>
    </ul>
  </section>

  <section class="service col-home">
    <div class="service-head">
      <div class="service-icon"><svg width="30" height="28" viewBox="0 0 30 28"><path d="M4 6l1 2.5 2.5 1-2.5 1L4 13l-1-2.5L.5 9.5 3 8.5zM9 17l.8 2 2 .8-2 .8L9 23l-.8-2.4-2-.8 2-.8z" fill="#2a8545"/><path d="M26 2l2 2-8 9-2-2z" fill="#2a8545"/><path d="M11 13c4-3 9-2 10 2 1 4-2 9-9 11l-3-5 3-1-4-1z" fill="#2a8545"/></svg></div>
      <div class="service-title">Betreuung &amp;<br>Hauswirtschaft</div>
    </div>
    <ul class="service-list">
      <li>Unterstützung bei hauswirtschaftlichen Aufgaben</li>
      <li>Hilfe bei Einkäufen oder Behördengängen</li>
      <li>Gemeinsame Aktivitäten und sozialer Austausch</li>
    </ul>
  </section>

  <section class="service col-basic">
    <div class="service-head">
      <div class="service-icon"><svg width="28" height="26" viewBox="0 0 28 26"><path d="M15 12c-5-3.5-7-5.5-7-8a3.5 3.5 0 0 1 7-.5 3.5 3.5 0 0 1 7 .5c0 2.5-2 4.5-7 8z" fill="#2a8545"/><path d="M1 16h5l5 2h6a2 2 0 0 1 0 4h-6 7l7-5a2 2 0 0 1 3 3l-8 6H1z" fill="#2a8545"/></svg></div>
      <div class="service-title">Grundpflege</div>
    </div>
    <ul class="service-list">
      <li>Assistenz bei Routinen wie Baden, Ankleiden und Körperpflege</li>
      <li>Unterstützung bei Mobilität und Erhalt der Selbstständigkeit</li>
      <li>Hilfe bei Nahrungs- und Flüssigkeitsaufnahme</li>
    </ul>
  </section>

  <svg class="shapes" width="818" height="1160" viewBox="0 0 818 1160">
    <path d="M0 1088 C270 1070 550 1070 818 1090 L818 1160 L0 1160Z" fill="var(--sage)" opacity="0.6"/>
    <path d="M0 1104 C270 1086 550 1086 818 1104 L818 1160 L0 1160Z" fill="var(--green)"/>
    <path d="M0 1112 C270 1094 550 1094 818 1112 L818 1160 L0 1160Z" fill="var(--orange)"/>
  </svg>

  <footer class="footer">
    <div class="contact"><svg viewBox="0 0 20 20"><circle cx="10" cy="10" r="9" fill="none" stroke="#fff" stroke-width="1.8"/><ellipse cx="10" cy="10" rx="4" ry="9" fill="none" stroke="#fff" stroke-width="1.5"/><path d="M1 10h18M3 5.5h14M3 14.5h14" stroke="#fff" stroke-width="1.5"/></svg>www.pflegevarnholt.de</div>
    <div class="contact"><svg viewBox="0 0 20 20"><circle cx="10" cy="10" r="9" fill="none" stroke="#fff" stroke-width="1.8"/><rect x="5" y="6.5" width="10" height="7" rx="1" fill="none" stroke="#fff" stroke-width="1.5"/><path d="M5 7l5 4 5-4" fill="none" stroke="#fff" stroke-width="1.5"/></svg>info@pflegevarnholt.de</div>
    <div class="contact"><svg viewBox="0 0 20 20"><circle cx="10" cy="10" r="10" fill="#fff"/><path d="M7 5l2 3-1.3 1.3a7 7 0 0 0 3 3L12 11l3 2-1 2c-4 0-8-4-8-8z" fill="#f07237"/></svg>0208 - 555 210 40</div>
  </footer>
</main>
</body>
</html>
```